Prominent Law Firm Needs a New Stationary Design

We need new stationary design to go with our new logo and rustic offices.
Things we need on the letterhead:
logo (see attached file), would also like the Seven-Figure Verdict Logo (attached) somewhere on the stationary,
5182 North Pelham Avenue
Tulsa, Oklahoma 74219
(918) 555-0143 Tel ★ (918) 555-0187 Fax
www.TWVQX.example

We also need the names of the 4 partners:
Dale K. Hollingsworth
Vernon P. Hollingsworth
Mark E. Fenwicke
Tyler D. Ashcombe

And the other staff:
Brenda K. Lyle
Tendaji K. Oyelowanta
Gordon Pettijo

Hilda V. Pruitt, RN

Of Counsel:
Wendell S. Hollingsworth

Industry/Entity Type

Law Firm

```html
<!DOCTYPE html>
<html lang="en">
<head>
<meta charset="utf-8">
<title>Hollingsworth Hollingsworth Fenwicke — Letterhead</title>
<link rel="stylesheet" href="https://fonts.googleapis.com/css2?family=Cinzel:wght@400;700&display=swap">
<style>
  :root {
    --backdrop: #e6e6e6;
    --paper: #ffffff;
    --ink: #1c1c1c;
    --ink-soft: #4a4a4a;
    --watermark: #ececec;
    --badge-outer: #2b2b2b;
    --badge-inner: #6e1f24;
  }
  * { margin: 0; padding: 0; box-sizing: border-box; }
  html, body {
    width: 1070px; height: 1200px; overflow: hidden;
    background: var(--backdrop);
  }
  .letterhead {
    position: absolute; left: 135px; top: 35px;
    width: 800px; height: 1130px;
    background: var(--paper);
    font-family: "Cinzel", serif;
    color: var(--ink-soft);
  }
  .award-badge { position: absolute; left: 42px; top: 40px; }
  .firm-mark {
    position: absolute; left: 250px; top: 70px; width: 300px;
    text-align: center; color: var(--ink);
  }
  .firm-mark .firm-name {
    font-size: 15px; font-weight: 700; letter-spacing: 0.5px; line-height: 1.35;
  }
  .firm-mark .firm-dot {
    display: block; width: 12px; height: 12px; margin: 10px auto 0;
    border-radius: 50%; background: var(--ink);
  }
  .contact {
    position: absolute; left: 563px; top: 40px;
    font-size: 12px; line-height: 17px; letter-spacing: 0.6px;
    list-style: none;
  }
  .watermark {
    position: absolute; left: 100px; top: 500px; width: 600px;
    text-align: center; color: var(--watermark);
    font-size: 40px; font-weight: 700; line-height: 1.25; letter-spacing: 1px;
  }
  .roster {
    position: absolute; top: 1030px; list-style: none;
    font-size: 12px; line-height: 17.5px; letter-spacing: 0.6px;
  }
  .roster.partners { left: 67px; }
  .roster.associates { left: 313px; }
  .roster.counsel { left: 540px; }
</style>
</head>
<body>
  <main class="letterhead">
    <svg class="award-badge" width="90" height="90" viewBox="0 0 90 90" role="img" aria-label="Seven-Figure Verdict Logo">
      <circle cx="45" cy="45" r="44" fill="var(--badge-outer)"/>
      <circle cx="45" cy="45" r="30" fill="var(--badge-inner)"/>
    </svg>

    <header class="firm-mark">
      <div class="firm-name">Hollingsworth<br>Hollingsworth Fenwicke</div>
      <span class="firm-dot"></span>
    </header>

    <ul class="contact">
      <li>A: 5182 North Pelham Avenue</li>
      <li>Tulsa, Oklahoma 74219</li>
      <li>T: (918) 555-0143</li>
      <li>F: (918) 555-0187</li>
      <li>W: www.TWVQX.example</li>
    </ul>

    <div class="watermark" aria-hidden="true">Hollingsworth<br>Hollingsworth<br>Fenwicke</div>

    <ul class="roster partners">
      <li>Dale K. Hollingsworth</li>
      <li>Vernon P. Hollingsworth</li>
      <li>Mark E. Fenwicke</li>
      <li>Tyler D. Ashcombe</li>
    </ul>
    <ul class="roster associates">
      <li>Brenda K. Lyle</li>
      <li>Tendaji K. Oyelowanta</li>
      <li>Gordon Pettijo</li>
      <li>Hilda V. Pruitt, RN</li>
    </ul>
    <ul class="roster counsel">
      <li>Of Counsel:</li>
      <li>Wendell S. Hollingsworth</li>
    </ul>
  </main>
</body>
</html>
```